Zentrova - Creative Automation

We are a software house for Audio Visual Systems integration/automation and home automation. we develop innovative software to automate a variety of devices mainly related to audio visuals and we design touch panel user interfaces to control these systems.

We would like to see designs that stick to our colours and theme, which you can find on our webpage www.zentrova.com.au

The final design should communicate touch panels, innovation, software and automation.

Industry/Entity Type

Software

Requirements
Must have
• The business card must show the following information:
Name example : Derek Malloway
Qualification example: B Eng ICT(CompSys) Dip EngPrac
Title example : Control Systems Programmer
Mobile Phone, Company phone, Email address ,Company website

```html
<!DOCTYPE html>
<html lang="en">
<head>
<meta charset="utf-8">
<title>Zentrova - Creative Automation business card</title>
<link href="https://fonts.googleapis.com/css2?family=Open+Sans:wght@400;600;700;800&display=swap" rel="stylesheet">
<style>
  :root {
    --brand-green: #1ea566;
    --brand-blue: #1d6fb8;
    --ink: #2a2a2a;
    --muted: #8a8a8a;
    --paper: #ffffff;
    --backdrop: #ecebe8;
    --divider: #e2e2e2;
  }
  * { margin: 0; padding: 0; box-sizing: border-box; }
  html, body { width: 1200px; height: 576px; overflow: hidden; }
  body {
    background: var(--backdrop);
    font-family: "Open Sans", sans-serif;
    position: relative;
  }
  .card {
    position: absolute;
    top: 145px;
    width: 500px;
    height: 286px;
    box-shadow: 0 6px 18px rgba(0,0,0,0.18);
  }
  .card-front {
    left: 60px;
    background: var(--brand-green);
    display: flex;
    align-items: center;
    justify-content: center;
  }
  .front-brand { text-align: center; color: var(--paper); }
  .front-brand .wordmark {
    font-size: 64px;
    font-weight: 800;
    letter-spacing: -1px;
    line-height: 1;
    text-transform: lowercase;
  }
  .front-brand .tagline {
    font-size: 13px;
    font-weight: 700;
    margin-top: 4px;
    text-align: right;
    padding-right: 8px;
  }
  .card-back {
    left: 640px;
    background: var(--paper);
    display: flex;
    align-items: center;
  }
  .back-brand {
    width: 250px;
    display: flex;
    flex-direction: column;
    align-items: center;
    padding-top: 30px;
  }
  .back-brand .wordmark {
    font-size: 38px;
    font-weight: 800;
    color: var(--brand-blue);
    letter-spacing: -1px;
    line-height: 1;
    text-transform: lowercase;
  }
  .back-brand .tagline {
    font-size: 9px;
    font-weight: 700;
    color: var(--brand-blue);
    margin-top: 3px;
  }
  .divider {
    width: 1px;
    height: 150px;
    background: var(--divider);
  }
  .contact { padding-left: 22px; }
  .contact .name {
    font-size: 19px;
    color: var(--brand-green);
    line-height: 1.1;
  }
  .contact .role { font-size: 12px; color: var(--ink); margin-top: 2px; }
  .contact .qualification { font-size: 9px; color: var(--muted); margin-top: 1px; }
  .contact-list { list-style: none; margin-top: 10px; }
  .contact-list li {
    display: flex;
    align-items: center;
    gap: 7px;
    font-size: 12.5px;
    color: var(--ink);
    line-height: 1.45;
  }
  .contact-list svg { width: 10px; height: 10px; fill: var(--brand-green); flex: none; }
</style>
</head>
<body>
  <section class="card card-front" aria-label="Card front">
    <div class="front-brand">
      <div class="wordmark">Zentrova</div>
      <div class="tagline">Creative Automation</div>
    </div>
  </section>

  <section class="card card-back" aria-label="Card back">
    <div class="back-brand">
      <div class="wordmark">Zentrova</div>
      <div class="tagline">Creative Automation</div>
    </div>
    <div class="divider"></div>
    <div class="contact">
      <div class="name">Derek Malloway</div>
      <div class="role">Control Systems Programmer</div>
      <div class="qualification">B Eng ICT(CompSys) Dip EngPrac</div>
      <ul class="contact-list">
        <li>
          <svg viewBox="0 0 10 10" aria-hidden="true"><path d="M3 0h4a1 1 0 0 1 1 1v8a1 1 0 0 1-1 1H3a1 1 0 0 1-1-1V1a1 1 0 0 1 1-1zm0 1.5v6h4v-6z"/></svg>
          +0400 555 018
        </li>
        <li>
          <svg viewBox="0 0 10 10" aria-hidden="true"><path d="M0 3c0-1 2-2 5-2s5 1 5 2v1H7.5V3h-5v1H0zM2 5h6l1 4H1z"/></svg>
          +0200 555 731
        </li>
        <li>
          <svg viewBox="0 0 10 10" aria-hidden="true"><path d="M0 2h10v6H0zm1 .8v.4l4 2.6 4-2.6v-.4L5 5.2z"/></svg>
          derek@zentrova.com
        </li>
        <li>
          <svg viewBox="0 0 10 10" aria-hidden="true"><circle cx="5" cy="5" r="5"/><path d="M1 5h8M5 1v8" stroke="#fff" stroke-width="0.8"/></svg>
          zentrova.com.au
        </li>
      </ul>
    </div>
  </section>
</body>
</html>
```